Kessler MD Summit Primary Care Business Card

Need a business card for a medical clinic targeting VIP patients. Should portray an upscale feeling. Simple, clean design. Logo and colors need to be incorporated into card. Clinic colors are gray/ silver, blues, white same as logo.
Clinic is a cash only VIP service clinic targeting higher income patients.
Tagline: "Where every patient matters - Care Beyond Routine"

Target Market(s)

VIP, upscale

Industry/Entity Type

Medical

Contact Information for Business Card

Would like to use for cards with raised print or metallic highlight.

Requirements
Must have
• Incorporate logo, Use colors in logo
Nice to have
• Metallic detail
Should not have
• too much details or colors, other stock photos or designs

```html
<!DOCTYPE html>
<html lang="en">
<head>
<meta charset="utf-8">
<title>Kessler MD Summit Primary Care – Business Card</title>
<link href="https://fonts.googleapis.com/css2?family=Cinzel:wght@500&family=Arimo:wght@400&display=swap" rel="stylesheet">
<style>
  :root {
    --stage: #5e5e5e;
    --card-white: #ffffff;
    --card-gray: #959b9d;
    --navy: #3d5468;
    --ink: #1e1e1e;
    --rule: #9aa3a8;
    --light: #ffffff;
  }
  * { box-sizing: border-box; margin: 0; padding: 0; }
  html, body { width: 1200px; height: 1200px; overflow: hidden; }
  body {
    background: var(--stage);
    font-family: "Arimo", Arial, sans-serif;
    position: relative;
  }
  .brand-lockup {
    position: absolute; top: 250px; left: 0; width: 1200px;
    text-align: center; color: var(--light);
    font-family: "Cinzel", Georgia, serif; font-weight: 500;
    letter-spacing: 2px; line-height: 1.25;
  }
  .brand-lockup .line-1 { font-size: 34px; }
  .brand-lockup .line-2 { font-size: 30px; }

  .card {
    position: absolute; top: 560px; width: 540px; height: 304px; overflow: hidden;
  }
  .card-front { left: 50px; background: var(--card-white); }
  .card-back { left: 610px; background: var(--card-gray); }

  .front-name {
    position: absolute; left: 26px; top: 92px; width: 230px; text-align: center;
    font-family: "Cinzel", Georgia, serif; font-weight: 500; color: var(--navy);
    line-height: 1.3; letter-spacing: 1px;
  }
  .front-name .line-1 { font-size: 18px; }
  .front-name .line-2 { font-size: 16px; }

  .portrait {
    position: absolute; right: 30px; top: 20px; width: 94px; height: 94px;
    border-radius: 50%; border: 2px solid var(--navy);
    background: radial-gradient(circle at 50% 45%, #c9a999 0%, #8a7568 55%, #6d625b 100%);
  }
  .doctor {
    position: absolute; right: 26px; top: 120px; text-align: right;
  }
  .doctor-name {
    font-family: "Cinzel", Georgia, serif; font-weight: 500; color: var(--navy);
    font-size: 23px; letter-spacing: 1px;
  }
  .doctor-role { font-size: 13px; color: var(--navy); margin-top: 1px; }

  .contact-row {
    position: absolute; left: 0; top: 196px; width: 540px;
    display: flex; justify-content: center; align-items: flex-start;
  }
  .contact-item {
    display: flex; flex-direction: column; align-items: center;
    font-size: 13px; color: var(--ink); text-align: center; line-height: 1.35;
    padding: 0 12px;
  }
  .contact-item svg { width: 18px; height: 18px; margin-bottom: 10px; fill: var(--navy); }
  .contact-item + .contact-item { border-left: 1px solid var(--rule); }

  .tagline-band {
    position: absolute; left: 0; bottom: 0; width: 540px; height: 35px;
    background: var(--navy); color: var(--light); font-size: 15px;
    display: flex; align-items: center; justify-content: center;
  }

  .back-name {
    position: absolute; left: 0; top: 112px; width: 540px; text-align: center;
    font-family: "Cinzel", Georgia, serif; font-weight: 500; color: var(--navy);
    line-height: 1.3; letter-spacing: 1px;
  }
  .back-name .line-1 { font-size: 20px; }
  .back-name .line-2 { font-size: 18px; }
  .back-tagline {
    position: absolute; left: 0; top: 232px; width: 540px; text-align: center;
    color: var(--light); font-size: 16px;
  }
</style>
</head>
<body>
  <div class="brand-lockup">
    <div class="line-1">Kessler MD</div>
    <div class="line-2">Summit Primary Care</div>
  </div>

  <section class="card card-front">
    <div class="front-name">
      <div class="line-1">Kessler MD</div>
      <div class="line-2">Summit Primary Care</div>
    </div>

    <div class="portrait" role="img" aria-label="Portrait photo of Dr. Kessler"></div>
    <div class="doctor">
      <div class="doctor-name">Dr. Kessler</div>
      <div class="doctor-role">Managing Director</div>
    </div>

    <div class="contact-row">
      <div class="contact-item">
        <svg viewBox="0 0 24 24" aria-hidden="true"><path d="M12 2a7 7 0 0 0-7 7c0 5 7 13 7 13s7-8 7-13a7 7 0 0 0-7-7zm0 9.5A2.5 2.5 0 1 1 12 6.5a2.5 2.5 0 0 1 0 5z"/></svg>
        <span class="text">4820 Ridgeway Avenue, Suite 210<br>Larkfield, TX 78999</span>
      </div>
      <div class="contact-item">
        <svg viewBox="0 0 24 24" aria-hidden="true"><path d="M6.6 10.8a15.1 15.1 0 0 0 6.6 6.6l2.2-2.2a1 1 0 0 1 1-.25 11.4 11.4 0 0 0 3.6.57 1 1 0 0 1 1 1V20a1 1 0 0 1-1 1A17 17 0 0 1 3 4a1 1 0 0 1 1-1h3.5a1 1 0 0 1 1 1c0 1.25.2 2.45.57 3.57a1 1 0 0 1-.25 1z"/></svg>
        <span class="text">(555) 014-2286</span>
      </div>
      <div class="contact-item">
        <svg viewBox="0 0 24 24" aria-hidden="true"><path d="M2 6l10 7 10-7v12H2z"/><path d="M2 5h20l-10 7z"/></svg>
        <span class="text">dr.k@kesslermd-spc.com</span>
      </div>
    </div>

    <div class="tagline-band">Where every patient matters - Care Beyond Routine</div>
  </section>

  <section class="card card-back">
    <div class="back-name">
      <div class="line-1">Kessler MD</div>
      <div class="line-2">Summit Primary Care</div>
    </div>
    <div class="back-tagline">Where every patient matters - Care Beyond Routine</div>
  </section>
</body>
</html>
```